Powerpoint visual improvements

I need a cover page, and our beliefs page and differentiating factors page / graphic design for our presentation. For the cover page I would just like an attractive design that incorporate our architectural concept with columns and potentially our logo. For the beliefs page I just want a more attractive presentatoin of the concepts. For the differentiating factors page I want a graphic that captures the points about how we are different from competitors. I have used the attached content to date, but I think it can be improved. The text is included in the graphic and I would also like to make sure the firm logo is incorporated.

Target Market(s)

Individual and institutional investors.

Industry/Entity Type

Investment Advisory

Requirements
Must have
• Our corporate colors are generally RGB 145,148,149; 66,68,76; 0,0,153; and 0,63,127. Our logo is attached. Our primary font is Georgia. Our website is www.PelmarCW.com. The key pages are www.PelmarCW.com/beliefs and www.PelmarCW.com/value we are trying to capture in a presentation. We also need a new presentation cover. Use the website as a reference for the type of imagery we like.

```html
<!DOCTYPE html>
<html lang="en">
<head>
<meta charset="utf-8">
<title>Pelmar Capital Wealth – Differentiating Factors</title>
<link rel="stylesheet" href="https://fonts.googleapis.com/css2?family=Arimo:wght@400&display=swap">
<style>
  :root {
    --bg-light: #f1f7f4;
    --bg-mint: #d9ede4;
    --bg-green: #5fae8c;
    --bg-green-deep: #3f9470;
    --label-navy: #14288a;
    --icon-navy: #0d2a8c;
    --stone-light: #f7f9fa;
    --stone-mid: #e3e8ea;
    --stone-shade: #cfd6da;
    --brand-white: #ffffff;
  }
  * { box-sizing: border-box; margin: 0; padding: 0; }
  html, body { width: 1200px; height: 686px; overflow: hidden; }
  body { font-family: "Arimo", Arial, sans-serif; }

  .slide {
    position: relative;
    width: 1200px;
    height: 686px;
    overflow: hidden;
    background:
      radial-gradient(ellipse 420px 520px at -40px 640px, var(--bg-green) 0%, rgba(95,174,140,0.55) 35%, rgba(217,237,228,0) 75%),
      radial-gradient(ellipse 520px 380px at 1240px 40px, var(--bg-green-deep) 0%, rgba(95,174,140,0.5) 35%, rgba(217,237,228,0) 75%),
      radial-gradient(ellipse 700px 500px at 560px 260px, #ffffff 0%, var(--bg-light) 55%, var(--bg-mint) 100%);
  }

  .brand {
    position: absolute;
    left: 978px;
    top: 36px;
    display: flex;
    align-items: center;
    gap: 8px;
    color: var(--brand-white);
    font-weight: 400;
  }
  .brand-dot {
    width: 74px; height: 74px;
    border-radius: 50%;
    background: var(--brand-white);
  }
  .brand-name { font-size: 30px; line-height: 1; }
  .brand-sub { font-size: 8.5px; letter-spacing: 0.4px; margin-top: 5px; }

  .pillar {
    position: absolute;
    left: calc(var(--x) - 100px);
    width: 200px;
    top: 0;
    height: 686px;
  }
  .pillar-head {
    position: absolute;
    left: 0; right: 0;
    bottom: calc(686px - var(--top) + 12px);
    display: flex;
    flex-direction: column;
    align-items: center;
    gap: 8px;
  }
  .pillar-icon { width: 34px; height: 34px; color: var(--icon-navy); }
  .pillar-label {
    color: var(--label-navy);
    font-size: 17px;
    line-height: 20px;
    text-align: center;
  }
  .pillar-column {
    position: absolute;
    top: var(--top);
    left: 15px;
    width: 170px;
    bottom: 0;
    background: linear-gradient(90deg, var(--stone-shade) 0%, var(--stone-light) 40%, var(--stone-mid) 75%, var(--stone-shade) 100%);
  }
</style>
</head>
<body>
<main class="slide">

  <div class="brand" aria-label="Pelmar Capital Wealth">
    <span class="brand-dot"></span>
    <span>
      <div class="brand-name">Pelmar</div>
      <div class="brand-sub">CAPITAL WEALTH</div>
    </span>
  </div>

  <section class="pillar" style="--x:111px; --top:410px;">
    <div class="pillar-head">
      <svg class="pillar-icon" viewBox="0 0 34 34" fill="currentColor" aria-hidden="true">
        <path d="M12 4h10l-3 6h-4z"/><path d="M14 11h6c6 5 9 12 8 18H6c-1-6 2-13 8-18z"/>
      </svg>
      <div class="pillar-label">Experienced<br>Investors</div>
    </div>
    <div class="pillar-column" role="img" aria-label="Photograph of a classical Ionic stone column"></div>
  </section>

  <section class="pillar" style="--x:306px; --top:333px;">
    <div class="pillar-head">
      <svg class="pillar-icon" viewBox="0 0 34 34" fill="currentColor" aria-hidden="true">
        <rect x="3" y="3" width="13" height="13"/><rect x="18" y="18" width="13" height="13"/>
        <rect x="3" y="18" width="13" height="13" fill="none" stroke="currentColor" stroke-width="2"/>
        <rect x="18" y="3" width="13" height="13" fill="none" stroke="currentColor" stroke-width="2"/>
      </svg>
      <div class="pillar-label">Independent<br>Portfolio<br>Construction</div>
    </div>
    <div class="pillar-column" role="img" aria-label="Photograph of a classical Ionic stone column"></div>
  </section>

  <section class="pillar" style="--x:511px; --top:266px;">
    <div class="pillar-head">
      <svg class="pillar-icon" viewBox="0 0 34 34" fill="none" stroke="currentColor" stroke-width="2" aria-hidden="true">
        <path d="M5 13h6l8-6v20l-8-6H5z"/><path d="M23 12c2 3 2 7 0 10"/><path d="M27 9c4 5 4 11 0 16"/>
      </svg>
      <div class="pillar-label">Sound<br>Operational<br>Construction</div>
    </div>
    <div class="pillar-column" role="img" aria-label="Photograph of a classical Ionic stone column"></div>
  </section>

  <section class="pillar" style="--x:704px; --top:313px;">
    <div class="pillar-head">
      <svg class="pillar-icon" viewBox="0 0 34 34" fill="none" stroke="currentColor" stroke-width="2.5" aria-hidden="true">
        <circle cx="20" cy="14" r="10"/><path d="M12 22L4 30" stroke-width="4"/><path d="M15 18l4-4 3 2 4-5" stroke-width="1.8"/>
      </svg>
      <div class="pillar-label">Proactive Total<br>Fee Management</div>
    </div>
    <div class="pillar-column" role="img" aria-label="Photograph of a classical Ionic stone column"></div>
  </section>

  <section class="pillar" style="--x:901px; --top:250px;">
    <div class="pillar-head">
      <svg class="pillar-icon" viewBox="0 0 34 34" fill="none" stroke="#1b1f2a" stroke-width="2.5" aria-hidden="true">
        <circle cx="14" cy="14" r="10"/><path d="M21 21l9 9" stroke-width="4"/><path d="M10 18v-4M14 18v-7M18 18v-5" stroke-width="2"/>
      </svg>
      <div class="pillar-label">Institutional<br>Research Process</div>
    </div>
    <div class="pillar-column" role="img" aria-label="Photograph of a classical Ionic stone column"></div>
  </section>

  <section class="pillar" style="--x:1104px; --top:307px;">
    <div class="pillar-head">
      <svg class="pillar-icon" viewBox="0 0 34 34" fill="none" stroke="currentColor" stroke-width="2" aria-hidden="true">
        <circle cx="17" cy="10" r="2.5" fill="currentColor"/><path d="M12 5c-3 3-3 7 0 10M22 5c3 3 3 7 0 10M8 2c-5 5-5 11 0 16M26 2c5 5 5 11 0 16"/>
        <path d="M17 13l-6 19M17 13l6 19M13 25h8" stroke-width="2.5"/>
      </svg>
      <div class="pillar-label">Transparent<br>Communication</div>
    </div>
    <div class="pillar-column" role="img" aria-label="Photograph of a classical Ionic stone column"></div>
  </section>

</main>
</body>
</html>
```